Hip surgeon needs a educative book cover design

I need to re-design my old book cover for its 3rd edition.
It's a small book dedicated to my patients, who underwent total hip replacement. It's meant to help people getting around the basic care after a total hip replacement surgery and getting back to their normal, active life.
The title is: "Bright mornings: a walking companion guide".
I already had a new logo, new stationery and new website design from PixelHarbor (please see the attachments).
The final design should be look alike the other fresh new designs. It must communicate health, peacefulness.
I also attached the manual as it looks today for reference.
A5 size.
Just cover and back cover.

```html
<!DOCTYPE html>
<html lang="en">
<head>
<meta charset="utf-8">
<title>Bright Mornings – Book Cover</title>
<link rel="stylesheet" href="https://fonts.googleapis.com/css2?family=Open+Sans:wght@400;600&display=swap">
<style>
  :root {
    --page-bg: #eef1f4;
    --blue-deep: #1358b8;
    --blue-main: #1a68c8;
    --blue-band: #1552ab;
    --blue-soft: #2f92e2;
    --blue-soft-edge: #2580d6;
    --blue-glow: #4aaaf0;
    --blue-light: #4cb0ee;
    --blue-title: #a9e0ff;
    --blue-caption: #8fd3fb;
    --line: #7fcaf6;
    --ink-navy: #0c2f66;
    --white: #ffffff;
    --art-a: #e9eef3;
    --art-b: #c9d5e0;
  }
  * { box-sizing: border-box; margin: 0; padding: 0; }
  html, body { width: 1200px; height: 801px; overflow: hidden; }
  body {
    background: var(--page-bg);
    font-family: "Open Sans", Arial, sans-serif;
    position: relative;
  }
  .book-spread {
    position: absolute;
    left: 123px; top: 80px;
    width: 954px; height: 640px;
    display: flex;
    box-shadow: 0 10px 30px rgba(10, 40, 90, 0.18);
  }
  .cover { position: relative; width: 452px; height: 640px; background: var(--blue-main); overflow: hidden; }
  .spine {
    position: relative; width: 50px; height: 640px;
    background: var(--blue-deep);
    display: flex; align-items: center; justify-content: center;
  }
  .spine-title {
    writing-mode: vertical-rl;
    color: var(--white);
    font-weight: 600; font-size: 17px; letter-spacing: 0.3px;
    white-space: nowrap;
  }
  .band { position: absolute; left: 0; width: 100%; }
  .rule { position: absolute; left: 0; width: 100%; height: 2px; background: var(--line); opacity: 0.6; }

  .author {
    position: absolute; left: 0; width: 100%;
    display: flex; align-items: center; justify-content: center; gap: 8px;
    color: var(--white);
  }
  .author-dot { width: 18px; height: 18px; border-radius: 50%; background: var(--white); }
  .author-text { line-height: 1.1; }
  .author-name { font-size: 11px; font-weight: 600; display: block; }
  .author-role { font-size: 8px; font-weight: 400; display: block; opacity: 0.85; }

  /* back cover */
  .back .top-field { top: 0; height: 190px; background: var(--blue-main); }
  .back .title-block { position: absolute; top: 62px; left: 0; width: 100%; text-align: center; color: var(--white); }
  .back .main-title { font-size: 26px; font-weight: 600; line-height: 1.15; }
  .back .sub-title { font-size: 14px; font-weight: 400; margin-top: 6px; color: var(--blue-caption); }
  .back .mid-field {
    top: 196px; height: 300px;
    background:
      radial-gradient(ellipse 70% 80% at 38% 55%, var(--blue-glow) 0%, rgba(74,170,240,0) 70%),
      linear-gradient(180deg, var(--blue-soft) 0%, var(--blue-soft-edge) 100%);
  }
  .back .mid-rule { position: absolute; left: 0; width: 100%; height: 1px; background: var(--line); opacity: 0.35; }
  .back .lower-field { top: 496px; height: 144px; background: var(--blue-deep); }
  .back .author { top: 562px; }

  /* front cover */
  .front .head-field { top: 0; height: 62px; background: var(--blue-deep); }
  .front .author { top: 20px; }
  .front .title-field { top: 70px; height: 140px; background: var(--blue-band); }
  .front .main-title {
    position: absolute; top: 86px; left: 0; width: 100%;
    text-align: center; color: var(--blue-title);
    font-size: 38px; font-weight: 600; line-height: 1.12;
  }
  .front .subtitle-field { top: 210px; height: 48px; background: var(--blue-light); }
  .front .sub-title {
    position: absolute; top: 220px; left: 0; width: 100%;
    text-align: center; color: var(--ink-navy);
    font-size: 21px; font-weight: 400;
  }
  .front .illustration {
    position: absolute; left: 36px; top: 300px; width: 380px; height: 260px;
    background: linear-gradient(135deg, var(--art-a), var(--art-b));
    border: 2px solid var(--white);
  }
  .front .foot-field { top: 598px; height: 42px; background: var(--blue-deep); }
</style>
</head>
<body>
  <main class="book-spread">
    <section class="cover back" aria-label="Back cover">
      <div class="band top-field"></div>
      <div class="title-block">
        <h2 class="main-title">Bright Mornings</h2>
        <p class="sub-title">A Walking Companion Guide</p>
      </div>
      <div class="rule" style="top:192px"></div>
      <div class="band mid-field"></div>
      <div class="mid-rule" style="top:230px"></div>
      <div class="mid-rule" style="top:462px"></div>
      <div class="rule" style="top:496px"></div>
      <div class="band lower-field"></div>
      <div class="author">
        <span class="author-dot"></span>
        <span class="author-text"><span class="author-name">Dr. Lucas M. Ferraz</span><span class="author-role">Cirurgia do Quadril</span></span>
      </div>
    </section>

    <section class="spine" aria-label="Spine">
      <span class="spine-title">Bright Mornings : A Walking Companion Guide</span>
    </section>

    <section class="cover front" aria-label="Front cover">
      <div class="band head-field"></div>
      <div class="author">
        <span class="author-dot"></span>
        <span class="author-text"><span class="author-name">Dr. Lucas M. Ferraz</span><span class="author-role">Cirurgia do Quadril</span></span>
      </div>
      <div class="rule" style="top:66px"></div>
      <div class="band title-field"></div>
      <h1 class="main-title">Bright<br>Mornings</h1>
      <div class="band subtitle-field"></div>
      <p class="sub-title">A Walking Companion Guide</p>
      <div class="rule" style="top:262px"></div>
      <div class="illustration" role="img" aria-label="Line drawings of a hip implant and of a patient walking with crutches, exercising and climbing stairs"></div>
      <div class="band foot-field"></div>
    </section>
  </main>
</body>
</html>
```